Website Design Request - Management Consulting Firm

We need a Website designed for an IT Management Staffing and Recruiting firm called VENTRIX based in San Francisco.

The firm is an high-end technology staffing agency. Our focus is on quality and high-caliber candidates rather than quantity.

The website will have two main home pages. One for the recruiter and another on for the candidates.

The website needs to optimize for mobile devices as well.

I have attached few mock-ups that I have done just to show what I am thinking. The UI needs to be very clean, fluid, and it needs to have a modern, rustic, professional feel to it.

Target Market(s)

Technology Manager, Director, VP, CIO of Companies that have $4b-10b dollar revenue. Such as oakmeadowhome.example , https://www.lumbervale.example/, tidewell.example, norv.example

Industry/Entity Type

Management Consulting

Number of Pages Required

5+ page

Font styles to use
Sans Serif

Colors
f37122
ffffff

Requirements
Must have
• Please review mock-ups for suggestions
Nice to have
Should not have

```html
<!DOCTYPE html>
<html lang="en">
<head>
<meta charset="utf-8">
<title>VENTRIX — IT Project Management Jobs</title>
<link rel="stylesheet" href="https://fonts.googleapis.com/css2?family=Montserrat:wght@400;500;600;700&family=Open+Sans:wght@400;600&display=swap">
<style>
  :root {
    --brand: #f37122;
    --brand-dark: #dc5e16;
    --ink: #3d3d3d;
    --ink-soft: #777777;
    --nav-ink: #333333;
    --white: #ffffff;
    --footer-bg: #f5f5f5;
    --footer-line: #e2e2e2;
    --social: #c9c9c9;
  }
  * { box-sizing: border-box; margin: 0; padding: 0; }
  html, body { width: 1057px; height: 1200px; overflow: hidden; background: var(--white); }
  body { position: relative; font-family: "Open Sans", Arial, sans-serif; color: var(--ink); }
  .heading-font { font-family: "Montserrat", Arial, sans-serif; }

  .site-header { position: absolute; top: 0; left: 0; width: 1057px; height: 70px; background: var(--white); }
  .brand { position: absolute; left: 86px; top: 12px; }
  .brand-name { font-family: "Montserrat", Arial, sans-serif; font-weight: 600; font-size: 29px; letter-spacing: 1px; color: var(--brand); line-height: 1; }
  .brand-tagline { font-family: "Montserrat", Arial, sans-serif; font-size: 7.5px; letter-spacing: .4px; color: var(--nav-ink); margin-top: 3px; }
  .main-nav a { position: absolute; top: 32px; font-family: "Montserrat", Arial, sans-serif; font-size: 10.5px; color: var(--nav-ink); text-decoration: none; }

  .hero { position: absolute; top: 70px; left: 0; width: 1057px; height: 416px;
    background: radial-gradient(ellipse at 50% 55%, #6a6a6a 0%, #444444 45%, #2b2b2b 100%); }
  .hero-title { position: absolute; top: 155px; width: 100%; text-align: center; font-family: "Montserrat", Arial, sans-serif; font-weight: 700; font-size: 24px; color: var(--white); }
  .hero-sub { position: absolute; top: 196px; width: 100%; text-align: center; font-family: "Montserrat", Arial, sans-serif; font-size: 14px; color: var(--white); letter-spacing: .2px; }
  .hero-cta { position: absolute; left: 452px; top: 238px; width: 152px; height: 38px; background: var(--brand); color: var(--white);
    font-family: "Montserrat", Arial, sans-serif; font-weight: 700; font-size: 12px; display: flex; align-items: center; justify-content: center; }
  .hero-employers { position: absolute; top: 311px; width: 100%; text-align: center; font-size: 11px; color: var(--white); }
  .hero-employers strong { font-weight: 600; }
  .slider-dots { position: absolute; top: 390px; left: 505px; display: flex; gap: 5px; }
  .slider-dots span { width: 8px; height: 8px; border-radius: 50%; background: #8a8a8a; }
  .slider-dots span.active { background: var(--brand); }

  .info-tabs { position: absolute; top: 486px; left: 0; width: 1057px; height: 76px; display: flex; }
  .info-tab { flex: 1; position: relative; background: var(--brand); color: var(--white); text-align: center; }
  .info-tab.active { background: var(--brand-dark); }
  .info-tab svg { position: absolute; top: 14px; left: 50%; transform: translateX(-50%); }
  .info-tab span { position: absolute; top: 48px; left: 0; width: 100%; font-family: "Montserrat", Arial, sans-serif; font-size: 11.5px; }

  .steps-title { position: absolute; top: 631px; width: 100%; text-align: center; font-family: "Montserrat", Arial, sans-serif; font-weight: 700; font-size: 26px; color: var(--ink); }
  .steps-sub { position: absolute; top: 672px; width: 100%; text-align: center; font-family: "Montserrat", Arial, sans-serif; font-weight: 600; font-size: 13.5px; color: var(--ink); }
  .step { position: absolute; left: 333px; width: 400px; }
  .step-marker { position: absolute; left: 0; top: -1px; width: 18px; height: 18px; border: 1.5px solid var(--brand); border-radius: 50%; }
  .step-title { margin-left: 30px; font-family: "Montserrat", Arial, sans-serif; font-weight: 600; font-size: 12px; color: var(--ink); line-height: 16px; }
  .step-text { margin-left: 30px; margin-top: 8px; font-size: 11px; color: var(--ink-soft); line-height: 21px; }

  .upload-cta { position: absolute; left: 414px; top: 981px; width: 228px; height: 53px; background: var(--brand); color: var(--white);
    display: flex; align-items: center; justify-content: center; gap: 10px; font-family: "Montserrat", Arial, sans-serif; font-weight: 700; font-size: 12.5px; }

  .site-footer { position: absolute; top: 1098px; left: 0; width: 1057px; height: 102px; background: var(--footer-bg); border-top: 1px solid var(--footer-line); font-size: 10px; color: var(--ink-soft); }
  .footer-nav a, .footer-legal a, .footer-legal span { position: absolute; color: var(--ink-soft); text-decoration: none; }
  .social { position: absolute; left: 658px; top: 44px; display: flex; align-items: center; gap: 8px; }
  .social i { width: 24px; height: 24px; border-radius: 50%; background: var(--social); display: block; }
</style>
</head>
<body>
  <header class="site-header">
    <div class="brand">
      <div class="brand-name">VENTRIX</div>
      <div class="brand-tagline">PROJECT MANAGEMENT CONSULTING</div>
    </div>
    <nav class="main-nav">
      <a href="#" style="left:562px">PROFESSIONAL</a>
      <a href="#" style="left:702px">EMPLOYERS</a>
      <a href="#" style="left:827px">SIGN IN</a>
      <a href="#" style="left:929px">SIGN UP</a>
    </nav>
  </header>

  <section class="hero" role="img" aria-label="Overhead view of business people at a table fitting large puzzle pieces together">
    <h1 class="hero-title">LOOKING FOR IT PROJECTS MANAGEMENT JOBS?</h1>
    <p class="hero-sub">UPLOAD YOUR RESUME, ACCEPT INTERVIEW REQUESTS, GET OFFERS</p>
    <a class="hero-cta">GET OFFERS NOW</a>
    <p class="hero-employers"><strong>Looking for talents?</strong> see how it works for employers</p>
    <div class="slider-dots"><span class="active"></span><span></span><span></span><span></span></div>
  </section>

  <div class="info-tabs">
    <div class="info-tab active">
      <svg width="30" height="28" viewBox="0 0 30 28" fill="none" stroke="#fff" stroke-width="3">
        <circle cx="10" cy="15" r="5"/>
        <path d="M10 6v3M10 21v3M1 15h3M16 15h3M3.6 8.6l2.1 2.1M14.3 19.3l2.1 2.1M3.6 21.4l2.1-2.1M14.3 10.7l2.1-2.1"/>
        <circle cx="23" cy="7" r="3" stroke-width="2"/>
        <circle cx="23" cy="21" r="3" stroke-width="2"/>
      </svg>
      <span>HOW IT WORKS?</span>
    </div>
    <div class="info-tab">
      <svg width="28" height="26" viewBox="0 0 28 26" fill="none" stroke="#fff" stroke-width="1.5">
        <path d="M2 2h24v17H16l-4 4v-4H2z"/>
        <text x="14" y="15" text-anchor="middle" fill="#fff" stroke="none" font-family="Montserrat, Arial, sans-serif" font-weight="700" font-size="12">?</text>
      </svg>
      <span>WHY US?</span>
    </div>
  </div>

  <h2 class="steps-title">3 SIMPLE STEPS</h2>
  <p class="steps-sub">Employers pay 25% more for a better FIT Project Manager</p>

  <div class="step" style="top:736px">
    <span class="step-marker"></span>
    <div class="step-title">UPLOAD YOUR RESUME</div>
    <p class="step-text">answer few questions and upload your resume</p>
  </div>
  <div class="step" style="top:808px">
    <span class="step-marker"></span>
    <div class="step-title">WE SEND YOU INTERVIEW REQUESTS</div>
    <p class="step-text">Interested in someone? with a single click, send interview request<br>and let us handle the rest.</p>
  </div>
  <div class="step" style="top:898px">
    <span class="step-marker"></span>
    <div class="step-title">GET $1000 BONUS</div>
    <p class="step-text">Find a Job and get $1000 bonus Ventrix</p>
  </div>

  <a class="upload-cta">
    <svg width="26" height="22" viewBox="0 0 26 22" fill="#fff">
      <path d="M13 0l6 6h-4v7h-4V6H7z"/>
      <path d="M0 12h8v3h10v-3h8v10H0z"/>
    </svg>
    UPLOAD YOUR RESUME
  </a>

  <footer class="site-footer">
    <nav class="footer-nav">
      <a href="#" style="left:86px;top:28px">Professional</a>
      <a href="#" style="left:184px;top:28px">Employers</a>
      <a href="#" style="left:273px;top:28px">Sign In</a>
      <a href="#" style="left:344px;top:28px">Sign Up</a>
    </nav>
    <div class="footer-legal">
      <span style="left:86px;top:60px">© 2016. Ventrix. All rights reserved.</span>
      <a href="#" style="left:262px;top:60px">Privacy Policy</a>
      <span style="left:336px;top:60px">/</span>
      <a href="#" style="left:352px;top:60px">Terms &amp; Conditions</a>
      <span style="left:455px;top:60px">/</span>
      <a href="#" style="left:472px;top:60px">Disclaimer</a>
    </div>
    <div class="social">
      <span>Connect with our social network :</span>
      <i></i><i></i><i></i><i></i><i></i>
    </div>
  </footer>
</body>
</html>
```